Package design for quilted mattress covers.

We are producing a comfortable "quilted mattress protector" for beds . We need a very elegant and attractive and cozy insert label. approx. size is 14 inches high x11 inches wide. (One base design with slight edits to customize for each different bed size) It will be packaged in a nice clear bag, with the design label in front. I attached the type of product for reference

package text:
QUILTED MATTRESS COVER

size: 33x75x10"

*ultimate comfort
*breathable cotton top
*waterproof lining
*easy care wash and dry

Target Market(s)

displayed in drygood and bedding retail stores

Colors

Designer to choose colors to be used in the design.

Requirements
Must have
• all info as in description
Nice to have
• an image of a quilted cover on a bed, professionally included in the package design
Should not have
• ..

```html
<!DOCTYPE html>
<html lang="en">
<head>
<meta charset="utf-8">
<title>Velora Quilted Mattress Cover – Insert Label</title>
<link rel="stylesheet" href="https://fonts.googleapis.com/css2?family=Damion&family=Montserrat:wght@500;700;800&display=swap">
<style>
  :root {
    --backdrop: #ececec;
    --paper: #ffffff;
    --brand-blue: #2f64b5;
    --script-blue: #1f5fb8;
    --ink: #2b2b2b;
    --band-light: #8fa6d0;
    --band-mid: #4a6aae;
    --band-deep: #2a4688;
    --ring-blue: #3c63ad;
    --label-white: #ffffff;
  }
  * { margin: 0; padding: 0; box-sizing: border-box; }
  html, body {
    width: 1200px; height: 784px; overflow: hidden;
    background: var(--backdrop);
  }
  .canvas { position: relative; width: 1200px; height: 784px; }
  .insert-label {
    position: absolute; left: 323px; top: 36px;
    width: 554px; height: 712px;
    background: var(--paper);
    overflow: hidden;
    box-shadow: 0 2px 8px rgba(0,0,0,0.12);
  }
  .label-art { position: absolute; inset: 0; width: 554px; height: 712px; }
  .brand-name {
    position: absolute; left: 44px; top: 56px;
    font-family: "Montserrat", Arial, sans-serif;
    font-weight: 800; font-size: 36px; letter-spacing: -0.5px;
    color: var(--brand-blue);
  }
  .product-title {
    position: absolute; left: 0; right: 0; top: 200px;
    text-align: center; font-weight: normal;
  }
  .product-title .script {
    display: block;
    font-family: "Damion", cursive;
    font-size: 160px; line-height: 1;
    color: var(--script-blue);
    -webkit-text-stroke: 12px #fff;
    paint-order: stroke fill;
    transform: translateX(-4px) rotate(-5deg);
  }
  .product-title .subtitle {
    display: block; margin-top: -14px;
    padding-left: 190px;
    font-family: "Montserrat", Arial, sans-serif;
    font-weight: 500; font-size: 17px; letter-spacing: 0.5px;
    color: var(--ink);
  }
  .feature-list {
    position: absolute; left: 0; right: 0; top: 500px;
    display: flex; justify-content: space-around;
    padding: 0 14px; list-style: none;
  }
  .feature {
    width: 124px; text-align: center;
    font-family: "Montserrat", Arial, sans-serif;
    font-weight: 700; font-size: 12.5px; line-height: 1.15;
    color: var(--label-white);
  }
  .feature-photo {
    width: 96px; height: 96px; margin: 0 auto 10px;
    border-radius: 50%;
    border: 4px solid var(--ring-blue);
    box-shadow: inset 0 0 0 3px #fff;
  }
  .photo-comfort {
    background:
      radial-gradient(ellipse 30% 45% at 42% 40%, #e8b79a 0%, rgba(232,183,154,0) 100%),
      linear-gradient(160deg, #ffffff 0%, #f1efec 55%, #d9d6d2 100%);
  }
  .photo-cotton {
    background:
      linear-gradient(180deg, #e9edf2 0%, #ffffff 40%, #cfd6df 55%, #f4f6f8 75%, #d7dde4 100%);
  }
  .photo-water {
    background:
      radial-gradient(ellipse 45% 30% at 50% 50%, #6d93c9 0%, rgba(109,147,201,0) 100%),
      radial-gradient(circle at 50% 50%, #dfe9f6 0%, #ffffff 80%);
  }
  .photo-easycare {
    background:
      radial-gradient(ellipse 40% 22% at 55% 55%, #dfae8f 0%, rgba(223,174,143,0) 100%),
      linear-gradient(170deg, #fbfbfa 0%, #ecebe8 100%);
  }
  .size-note {
    position: absolute; left: 0; right: 0; bottom: 30px;
    text-align: center;
    font-family: "Montserrat", Arial, sans-serif;
    font-weight: 700; font-size: 15px; letter-spacing: 1px;
    color: var(--label-white);
  }
</style>
</head>
<body>
<main class="canvas">
  <section class="insert-label">
    <svg class="label-art" viewBox="0 0 554 712">
      <defs>
        <linearGradient id="bedroom-base" x1="0" y1="0" x2="0" y2="1">
          <stop offset="0" stop-color="#efece7"/>
          <stop offset="0.4" stop-color="#f6f5f3"/>
          <stop offset="0.75" stop-color="#e4e4e4"/>
          <stop offset="1" stop-color="#d6d4d1"/>
        </linearGradient>
        <radialGradient id="window-light" cx="0.75" cy="0.15" r="0.45">
          <stop offset="0" stop-color="#ffffff"/>
          <stop offset="1" stop-color="#ffffff" stop-opacity="0"/>
        </radialGradient>
        <radialGradient id="warm-side" cx="0" cy="0.75" r="0.35">
          <stop offset="0" stop-color="#d9c7ad"/>
          <stop offset="1" stop-color="#d9c7ad" stop-opacity="0"/>
        </radialGradient>
        <linearGradient id="band-fill" x1="0" y1="0" x2="0" y2="1">
          <stop offset="0" stop-color="var(--band-light)"/>
          <stop offset="0.35" stop-color="var(--band-mid)"/>
          <stop offset="1" stop-color="var(--band-deep)"/>
        </linearGradient>
      </defs>
      <g role="img" aria-label="Photo of a bed dressed with a white quilted mattress cover and pillows in a bright bedroom">
        <rect x="0" y="0" width="554" height="600" fill="url(#bedroom-base)"/>
        <rect x="0" y="0" width="554" height="600" fill="url(#window-light)"/>
        <rect x="0" y="0" width="554" height="600" fill="url(#warm-side)"/>
      </g>
      <polygon points="0,0 400,0 0,215" fill="#ffffff" opacity="0.95"/>
      <path d="M0,520 C120,500 220,500 330,520 C430,538 500,528 554,505 L554,712 L0,712 Z" fill="url(#band-fill)"/>
    </svg>

    <div class="brand-name">Velora</div>

    <h1 class="product-title">
      <span class="script">Quilted</span>
      <span class="subtitle">MATTRESS COVER</span>
    </h1>

    <ul class="feature-list">
      <li class="feature"><div class="feature-photo photo-comfort" role="img" aria-label="Hand pressing into soft mattress topper"></div>ULTIMATE<br>COMFORT</li>
      <li class="feature"><div class="feature-photo photo-cotton" role="img" aria-label="Close-up of quilted cotton top"></div>BREATHABLE<br>COTTON TOP</li>
      <li class="feature"><div class="feature-photo photo-water" role="img" aria-label="Water splash showing waterproof lining"></div>WATERPROOF<br>LINING</li>
      <li class="feature"><div class="feature-photo photo-easycare" role="img" aria-label="Hand resting on smooth washed cover"></div>EASY CARE<br>WASH AND DRY</li>
    </ul>

    <p class="size-note">SIZE: 33x75x10"</p>
  </section>
</main>
</body>
</html>
```